Business Cards Needed For Veterinary Business

Looking for a business card design for a veterinary blood bank. We would like it to be clean and professional on appearance but still warm and inviting. We would like to utilize our logo and similar coloring. We will use our phone number, email, website, employee name, employee title.

We do not want a bunch of animated animal photos but do not need the style to be as clinical as a laboratory or human medical procedure office.

We are looking for some creative ideas to choose from so that we can generate a standout professional business card for our management team to utilize.

Target Market(s)

professionals

Industry/Entity Type

veterinary

Contact Information for Business Card

employee name, employee title, phone number, website URL, email

Font styles to use
Sans Serif

Colors
0054AA
0677BA
7BADD7
CADEEF
E8F1F8
EB3D1F
EC4F4E
F09395
F8D3D4
FCEDEE

Requirements
Nice to have
• creative design
Should not have
• animated photos

```html
<!DOCTYPE html>
<html lang="en">
<head>
<meta charset="utf-8">
<title>Harbor Pet Blood Reserve – Business Card</title>
<link href="https://fonts.googleapis.com/css2?family=Montserrat:wght@500;600;800&display=swap" rel="stylesheet">
<style>
  :root{
    --bg:#e6e7e9;
    --red:#ec1f2b;
    --red-deep:#d81a25;
    --blue:#0054aa;
    --blue-mid:#0677ba;
    --ink:#2b2b2b;
    --muted:#555b63;
    --white:#ffffff;
    --line:#c9ccd1;
  }
  *{box-sizing:border-box;margin:0;padding:0}
  html,body{width:900px;height:1200px;overflow:hidden}
  body{background:var(--bg);font-family:"Montserrat",Arial,sans-serif;position:relative}
  .card{position:absolute;left:102px;width:696px;height:390px;border-radius:18px;overflow:hidden;box-shadow:0 10px 26px rgba(0,0,0,.18)}
  .card--front{top:165px;background:var(--red)}
  .card--back{top:610px;background:var(--white)}

  .front-brand{position:absolute;inset:0;display:flex;align-items:center;justify-content:center;gap:22px}
  .front-brand__dot{width:58px;height:58px;border-radius:50%;background:var(--red-deep)}
  .front-brand__name{color:var(--red-deep);font-weight:800;font-size:34px;line-height:1.1;letter-spacing:.5px;text-transform:uppercase}

  .back-brand{position:absolute;left:38px;top:112px;display:flex;align-items:center;gap:16px;width:290px}
  .back-brand__dot{flex:none;width:50px;height:50px;border-radius:50%;background:var(--red)}
  .back-brand__name{color:var(--blue);font-weight:800;font-size:24px;line-height:1.12;text-transform:uppercase}

  .divider{position:absolute;left:350px;top:84px;width:2px;height:170px;background:var(--line)}

  .person{position:absolute;left:374px;top:92px}
  .person__name{color:var(--blue);font-weight:800;font-size:25px;letter-spacing:.5px;text-transform:uppercase}
  .person__title{color:var(--muted);font-weight:500;font-size:15px;margin-top:4px}

  .contacts{position:absolute;left:374px;top:172px;list-style:none}
  .contacts li{display:flex;align-items:center;gap:12px;font-size:15px;font-weight:500;color:var(--muted);height:27px}
  .contacts svg{width:16px;height:16px;flex:none}

  .swoosh{position:absolute;left:0;bottom:0;width:696px;height:120px}
</style>
</head>
<body>
  <section class="card card--front" aria-label="Card front">
    <div class="front-brand">
      <span class="front-brand__dot"></span>
      <span class="front-brand__name">Harbor Pet<br>Blood Reserve</span>
    </div>
  </section>

  <section class="card card--back" aria-label="Card back">
    <div class="back-brand">
      <span class="back-brand__dot"></span>
      <span class="back-brand__name">Harbor Pet<br>Blood Reserve</span>
    </div>

    <div class="divider"></div>

    <div class="person">
      <h1 class="person__name">Colin R. Marsh</h1>
      <p class="person__title">President</p>
    </div>

    <ul class="contacts">
      <li>
        <svg viewBox="0 0 24 24" aria-hidden="true"><path fill="#ec1f2b" d="M6.6 10.8a15 15 0 0 0 6.6 6.6l2.2-2.2a1 1 0 0 1 1-.25 11.4 11.4 0 0 0 3.6.6 1 1 0 0 1 1 1V20a1 1 0 0 1-1 1A17 17 0 0 1 3 4a1 1 0 0 1 1-1h3.5a1 1 0 0 1 1 1c0 1.25.2 2.45.6 3.6a1 1 0 0 1-.25 1z"/></svg>
        555-014-2290
      </li>
      <li>
        <svg viewBox="0 0 24 24" aria-hidden="true"><rect x="2" y="5" width="20" height="14" rx="2" fill="#ec1f2b"/><path d="M3 6l9 7 9-7" stroke="#fff" stroke-width="1.8" fill="none"/></svg>
        hello@harborpetblood.com
      </li>
      <li>
        <svg viewBox="0 0 24 24" aria-hidden="true"><circle cx="12" cy="12" r="10" fill="#ec1f2b"/><path d="M2 12h20M12 2c3 3 3 17 0 20M12 2c-3 3-3 17 0 20" stroke="#fff" stroke-width="1.4" fill="none"/></svg>
        www.harborpetblood.com
      </li>
    </ul>

    <svg class="swoosh" viewBox="0 0 696 120" preserveAspectRatio="none" aria-hidden="true">
      <path d="M0 120 L0 104 C180 96 420 92 696 16 L696 120 Z" fill="#0054aa"/>
      <path d="M0 104 C200 92 430 84 696 8 L696 22 C430 98 200 106 0 114 Z" fill="#ffffff"/>
      <path d="M0 120 L0 114 C220 108 440 104 696 38 L696 120 Z" fill="#ec1f2b"/>
    </svg>
  </section>
</body>
</html>
```